Female Vocalist with/Big Band Concert Marketing Package

Description

We would like to promote our Big Band Concert with a Nationally well known female Vocalist. She won the TV competition Fjellsang being Norways best artist of 2012 : http://www.kvorblad.no/scene/artikkel.php?artid=48213907

Size requirements :
Poster : A2 and A3
Flyer : 9x14 cm
Newspaper ad : Module 12B : 34 x 80 mm

Delivery file format :
PDFs in CMYK ready for printing
Must be editable in Illustrator CS6

Headlines :
Lene Holvik - main headline
m/Brekkvik Messingorkester - big band sharing the act
Messingkvelden - theme of this evening

Concert Dates, Venues and Web adresses :
27.april - Torvhaug Musikkhall - www.torvhaug-musikkhall.no
28.april - Brekkvik Kulturhus - www.brekkvik-kulturhus.no

Press Pictures and Graphics of artist and band :
May be used or not used according to design

Venue Logos :
There shall be a logo for each venue

Ticket sales logos :
There shall be a logo for each ticket sales office

Sponsors :
There must be a free field with room for sponsor logos

Link to graphics and logos :
https://www.filkassen.example/sh/q4lnzrwp8dyk2ha/mvTJ3uPq8x

```html
<!DOCTYPE html>
<html lang="no">
<head>
<meta charset="utf-8">
<title>Lene Holvik – Messingkvelden</title>
<link rel="stylesheet" href="https://fonts.googleapis.com/css2?family=Jura:wght@400&family=Marcellus&family=Lato:wght@400;700&display=swap">
<style>
  :root {
    --page: #ffffff;
    --banner-dark: #0d0704;
    --banner-brown: #3a1c08;
    --glow: #c2620f;
    --glow-hot: #e8891f;
    --silver-top: #f2f2f2;
    --silver-bottom: #8e8e8e;
    --ink: #0b0b0b;
    --amber: #e78a1c;
    --amber-deep: #b9560a;
    --url: #f3c21b;
    --white: #ffffff;
    --sepia-light: #e9e2d8;
    --sepia-mid: #a89886;
    --sepia-dark: #2a211b;
  }
  html, body {
    margin: 0;
    padding: 0;
    width: 1200px;
    height: 538px;
    overflow: hidden;
    background: var(--page);
  }
  .canvas {
    position: relative;
    width: 1200px;
    height: 538px;
    background: var(--page);
  }
  .banner {
    position: absolute;
    left: 34px;
    top: 26px;
    width: 1132px;
    height: 484px;
    overflow: hidden;
    background:
      radial-gradient(ellipse 420px 300px at 400px 170px, var(--glow-hot) 0%, var(--glow) 30%, var(--banner-brown) 65%, transparent 100%),
      linear-gradient(90deg, var(--banner-dark) 0%, var(--banner-brown) 45%, var(--banner-dark) 75%);
  }
  .artist-photo {
    position: absolute;
    right: 0;
    top: 0;
    width: 540px;
    height: 484px;
    background:
      radial-gradient(ellipse 240px 280px at 250px 200px, var(--sepia-light) 0%, var(--sepia-mid) 55%, var(--sepia-dark) 100%);
    -webkit-mask-image: linear-gradient(90deg, transparent 0%, #000 22%);
    mask-image: linear-gradient(90deg, transparent 0%, #000 22%);
  }
  .band-photo {
    position: absolute;
    right: 0;
    top: 202px;
    width: 170px;
    height: 282px;
    background: linear-gradient(160deg, #5a4a3a 0%, #2a201a 60%, #120c08 100%);
    -webkit-mask-image: linear-gradient(90deg, transparent 0%, #000 35%);
    mask-image: linear-gradient(90deg, transparent 0%, #000 35%);
  }
  .artist-name {
    position: absolute;
    left: 80px;
    top: 84px;
    margin: 0;
    font-family: "Jura", sans-serif;
    font-weight: 400;
    font-size: 104px;
    line-height: 1;
    letter-spacing: 1px;
    background: linear-gradient(180deg, var(--silver-top) 20%, var(--silver-bottom) 100%);
    -webkit-background-clip: text;
    background-clip: text;
    color: transparent;
  }
  .band-name {
    position: absolute;
    right: 548px;
    top: 198px;
    margin: 0;
    font-family: "Lato", sans-serif;
    font-weight: 400;
    font-size: 25px;
    color: var(--ink);
  }
  .evening-theme {
    position: absolute;
    left: 88px;
    top: 266px;
    margin: 0;
    font-family: "Marcellus", serif;
    font-weight: 400;
    font-size: 68px;
    line-height: 1;
    color: var(--amber);
    text-shadow: 2px 3px 4px rgba(0,0,0,0.55);
  }
  .concert {
    position: absolute;
    top: 388px;
    display: flex;
    align-items: flex-start;
    gap: 8px;
    font-family: "Lato", sans-serif;
  }
  .concert--first { left: 98px; }
  .concert--second { left: 436px; }
  .venue-mark {
    width: 34px;
    display: flex;
    flex-direction: column;
    align-items: center;
    gap: 2px;
  }
  .venue-mark__square {
    width: 28px;
    height: 28px;
    background: var(--white);
  }
  .venue-mark--first .venue-mark__square { background: #e0e6ea; }
  .venue-mark--second .venue-mark__square { background: #d9c23a; }
  .venue-mark__name {
    font-size: 6px;
    color: var(--white);
    letter-spacing: 0.2px;
  }
  .concert__date {
    margin: 0;
    font-weight: 700;
    font-size: 20px;
    color: var(--white);
    white-space: nowrap;
  }
  .concert__url {
    margin: 6px 0 0 8px;
    font-weight: 700;
    font-size: 20px;
    color: var(--url);
    white-space: nowrap;
  }
  .tickets {
    position: absolute;
    left: 962px;
    top: 380px;
    font-family: "Lato", sans-serif;
  }
  .tickets__label {
    margin: 0 0 8px;
    font-size: 15px;
    color: var(--white);
  }
  .tickets__outlets {
    display: flex;
    gap: 10px;
  }
  .ticket-outlet {
    display: flex;
    align-items: center;
    justify-content: center;
    height: 40px;
    padding: 0 6px;
    font-size: 12px;
    font-weight: 700;
  }
  .ticket-outlet--round {
    color: var(--amber);
  }
  .ticket-outlet--box {
    background: var(--white);
    color: var(--ink);
  }
</style>
</head>
<body>
<div class="canvas">
  <section class="banner">
    <div class="artist-photo" role="img" aria-label="Portrettfoto av vokalisten Lene Holvik, smilende, med saksofon bak"></div>
    <div class="band-photo" role="img" aria-label="Foto av en trombonist fra Brekkvik Messingorkester"></div>

    <h1 class="artist-name">Lene Holvik</h1>
    <p class="band-name">m/Brekkvik Messingorkester</p>
    <h2 class="evening-theme">Messingkvelden</h2>

    <div class="concert concert--first">
      <div class="venue-mark venue-mark--first">
        <span class="venue-mark__square"></span>
        <span class="venue-mark__name">TORVHAUG</span>
      </div>
      <div>
        <p class="concert__date">27.april - Torvhaug Musikkhall</p>
        <p class="concert__url">www.torvhaug-musikkhall.no</p>
      </div>
    </div>

    <div class="concert concert--second">
      <div class="venue-mark venue-mark--second">
        <span class="venue-mark__square"></span>
        <span class="venue-mark__name">BREKKVIK</span>
      </div>
      <div>
        <p class="concert__date">28.april - Brekkvik Kulturhus</p>
        <p class="concert__url">www.brekkvik-kulturhus.no</p>
      </div>
    </div>

    <div class="tickets">
      <p class="tickets__label">tickets available at:</p>
      <div class="tickets__outlets">
        <span class="ticket-outlet ticket-outlet--round">Kvitbillett</span>
        <span class="ticket-outlet ticket-outlet--box">Billettbua</span>
      </div>
    </div>
  </section>
</div>
</body>
</html>
```